Remote Planning & Scheduling Power Point Presentation

This PP presentation is to help explain what RPS is and its benefits. Need help with a better illustration on slide 3 that explains the process, overall aesthetics, need better images, and cleaner workflow on slide 18. Keep the ZOL Logo in the bottom right of each slide. I have included a one-pager and infographic to help. I am still working of verbiage.

Thanks
JR

```html
<!DOCTYPE html>
<html lang="en">
<head>
<meta charset="utf-8">
<title>Remote Planning &amp; Scheduling – Slides</title>
<link href="https://fonts.googleapis.com/css2?family=Open+Sans:wght@400;600;700&display=swap" rel="stylesheet">
<style>
  :root{
    --ink:#222;
    --blue:#5b9bd5;
    --navy:#3b4a63;
    --navy-deep:#2e3b52;
    --teal:#9fcad0;
    --red:#e0201b;
    --grey-band:#c9ccd3;
    --grey-dark:#4d5568;
    --logo:#b7bfca;
    --white:#fff;
  }
  *{box-sizing:border-box;margin:0;padding:0}
  html,body{width:900px;height:1200px;overflow:hidden;background:var(--white)}
  body{position:relative;font-family:"Open Sans",Arial,sans-serif;color:var(--ink)}
  .slide{position:absolute;overflow:hidden;background:var(--white)}
  .brand{position:absolute;right:10px;bottom:6px;font-size:10px;font-weight:700;color:var(--logo);letter-spacing:.5px;z-index:3}
  .placeholder{position:absolute}

  /* Savings */
  .s-savings{left:0;top:0;width:445px;height:253px}
  .s-savings .placeholder{left:0;top:0;width:215px;height:253px;background:linear-gradient(160deg,#2f4f78 0%,#f3c9d5 45%,#9fc0dc 75%,#e9d8a6 100%)}
  .banner{position:absolute;left:240px;top:14px;width:205px;height:28px;background:var(--blue);border-radius:14px 0 0 14px;font-size:16px;font-weight:600;text-align:center;line-height:28px;color:var(--ink)}
  .checks{position:absolute;left:225px;top:56px;list-style:none;font-size:9px;line-height:16.8px;white-space:nowrap}
  .checks li::before{content:"✓";color:#3a6f2f;font-weight:700;margin-right:7px}
  .checks .cont{padding-left:15px}

  /* Packages */
  .s-standard{left:460px;top:0;width:440px;height:253px}
  .s-advanced{left:0;top:256px;width:445px;height:250px}
  .slide-title{position:absolute;left:16px;top:10px;font-size:20px;font-weight:400}
  .pkg{position:absolute;left:16px;top:50px;font-size:8.5px;line-height:12.4px;z-index:2}
  .pkg .num{color:var(--blue);font-size:12px;font-weight:700;margin-right:8px}
  .pkg h3{display:inline;font-size:9px;font-weight:700}
  .pkg p{margin-left:28px}
  .pkg ul{margin-left:44px;list-style:square}
  .s-advanced .pkg{top:46px}
  .s-advanced .pkg p{margin-left:16px}
  .s-advanced .pkg ul{margin-left:32px}
  .bands{position:absolute;bottom:0}
  .s-standard .bands{right:0}
  .s-advanced .bands{left:0}

  /* Leveraging */
  .s-leverage{left:445px;top:256px;width:342px;height:250px;background:var(--navy)}
  .s-leverage::after{content:"";position:absolute;right:4px;top:0;width:4px;height:100%;background:var(--white)}
  .s-leverage h2{position:absolute;left:0;right:12px;top:14px;text-align:center;font-size:17px;font-weight:400;color:var(--white)}
  .cards{position:absolute;left:12px;top:58px;width:310px;display:grid;grid-template-columns:1fr 1fr;gap:18px 22px}
  .card{background:var(--white);border:6px solid var(--navy-deep);outline:1px solid #8894a8;height:74px;padding:6px 8px;font-size:7.2px;line-height:10px}

  /* Connected */
  .s-connected{left:0;top:507px;width:443px;height:246px;background:var(--teal)}
  .pill{position:absolute;left:0;top:8px;width:320px;height:26px;background:#3a3d42;border-radius:0 13px 13px 0;color:var(--white);font-size:15px;font-weight:700;line-height:26px;padding-left:8px;white-space:nowrap}
  .pill small{font-size:8px;font-weight:400;margin-left:6px}
  .node-label{position:absolute;font-size:8px;color:var(--ink);font-weight:600;white-space:nowrap}
  .tasks{position:absolute;left:40px;width:74px;top:164px;font-size:8.5px;line-height:10.6px;text-align:right;font-weight:600;z-index:2}

  /* Benefits */
  .s-benefits{left:445px;top:507px;width:455px;height:246px}
  .s-benefits h2{position:absolute;left:24px;top:20px;width:245px;font-size:15px;font-weight:700;line-height:19px}
  .benefits{position:absolute;left:24px;top:98px;width:225px;font-size:7.5px;line-height:11px;list-style:none}
  .benefits li{margin-bottom:7px;padding-left:10px;position:relative}
  .benefits li::before{content:"•";position:absolute;left:0}
  .s-benefits .placeholder{left:290px;top:0;width:165px;height:246px;background:linear-gradient(180deg,#3e4a5a 0%,#5b7a8c 30%,#8fb8c4 50%,#5a9a4c 75%,#3f8a3a 100%)}
</style>
</head>
<body>

<section class="slide s-savings">
  <div class="placeholder" role="img" aria-label="Illustration of a hand holding a piggy bank and shopping bags"></div>
  <div class="banner">Savings</div>
  <ul class="checks">
    <li>Pay for the time/Package you use</li>
    <li>No Per Diem</li>
    <li>No Overtime</li>
    <li>No Paid Holidays</li>
    <li>No Sick Leave</li>
    <li>No Vacations Hours</li>
    <li>No Taxes</li>
    <li>No Insurance</li>
    <li>No Risk</li>
    <li>No Safety Site Classes and No Background Checks<br><span class="cont">to Perform</span></li>
  </ul>
  <span class="brand">ZOL</span>
</section>

<section class="slide s-standard">
  <h2 class="slide-title">Packages: Planning Phase</h2>
  <div class="pkg">
    <span class="num">01</span><h3>Standard Package</h3>
    <p>Schedule Weekly Progress Report Contains the Following:</p>
    <ul>
      <li>Start Date of Schedule DevelopmentAssign a Start Data Date</li>
      <li>Number of Worklist Item in Schedule</li>
      <li>Worklist Items in Schedule with Details (Tasks) added</li>
      <li>Logic % Complete</li>
      <li>Trended Completion Date</li>
      <li>Worklist Items with Resources and all Activity Codes Progress</li>
      <li>Internal Logic only, From one Task to another e.g.... Blind Exchanger to Open Dollar Plate etc....</li>
      <li>Resource loaded Tasks</li>
      <li>Standard Activity Codes assigned to all Tasks</li>
      <li>Default Calendars assigned to all Activities (8 hours per day, 5 Days per Week) unless prearranged to use a TAR calendar as the default</li>
      <li>All following PMFRAME rules for project development</li>
    </ul>
  </div>
  <svg class="bands" width="60" height="40" viewBox="0 0 60 40"><polygon points="60,0 60,40 0,40" fill="var(--grey-band)"/><polygon points="60,18 60,40 28,40" fill="var(--grey-dark)"/></svg>
  <span class="brand" style="color:#eef0f3">ZOL</span>
</section>

<section class="slide s-advanced">
  <h2 class="slide-title">Packages: Planning Phase</h2>
  <div class="pkg">
    <span class="num">02</span><h3>Advanced Package:</h3>
    <p>All the Standard Package items plus:</p>
    <ul>
      <li>Internal Logic as well as external logic</li>
      <li>Resource leveling</li>
      <li>Histograms</li>
      <li>Milestone KPI's</li>
      <li>Customized Reporting</li>
      <li>Risk Reviewed</li>
    </ul>
  </div>
  <svg class="bands" width="445" height="120" viewBox="0 0 445 120">
    <polygon points="0,120 0,95 445,20 445,120" fill="#e6e7ea"/>
    <polygon points="0,120 180,120 445,60 445,35" fill="var(--grey-band)"/>
    <polygon points="0,120 0,105 445,45 445,55 120,120" fill="#ffffff"/>
    <polygon points="0,120 0,112 445,70 445,120" fill="var(--grey-dark)"/>
  </svg>
  <span class="brand" style="color:#dfe3e8">ZOL</span>
</section>

<section class="slide s-leverage">
  <h2>Leveraging the Industries Best</h2>
  <div class="cards">
    <div class="card">ZOL's office is located in Bay Harbor, TX, right in the heart of the Petro-Chemical and Refining Industry</div>
    <div class="card">We have access to many of the skilled resources needed for STO planning</div>
    <div class="card">This also eliminates paying per diem cost, no more temporary offices, no more overtime</div>
    <div class="card">Remote Planning also offers fixed prices, now you know how much planning will cost before getting started</div>
  </div>
  <span class="brand" style="right:18px">ZOL</span>
</section>

<section class="slide s-connected">
  <div class="pill">Keeping Everyone Connected<small>Remote Planning</small></div>
  <div class="placeholder" role="img" aria-label="Silhouettes of the leadership team" style="left:6px;top:48px;width:110px;height:62px;background:linear-gradient(180deg,#3a3d42,#22252a)"></div>
  <span class="node-label" style="left:32px;top:114px">Leadership Team</span>
  <div class="placeholder" role="img" aria-label="On-site planner climbing plan steps" style="left:148px;top:44px;width:80px;height:92px;background:linear-gradient(180deg,#2c3036,#6d8fa0)"></div>
  <span class="node-label" style="left:232px;top:58px">On Site Planner</span>
  <div class="placeholder" role="img" aria-label="Laptop showing a schedule work package" style="left:318px;top:38px;width:108px;height:66px;background:linear-gradient(180deg,#dfe6ee,#5a6b80)"></div>
  <span class="node-label" style="left:322px;top:108px">Complete Work Package</span>
  <div class="placeholder" role="img" aria-label="Planning dashboard with charts" style="left:152px;top:168px;width:90px;height:56px;background:linear-gradient(180deg,#eef3f7,#5fae58)"></div>
  <span class="node-label" style="left:174px;top:228px">TurnPlan</span>
  <div class="placeholder" role="img" aria-label="Remote planner team silhouettes with laptops" style="left:290px;top:140px;width:90px;height:88px;background:linear-gradient(180deg,#b9cfd2,#3a3d42)"></div>
  <span class="node-label" style="left:294px;top:230px">Remote Planner Team</span>
  <div class="placeholder" role="img" aria-label="Man reviewing a document" style="left:8px;top:148px;width:40px;height:92px;background:linear-gradient(180deg,#2c3036,#4a5058)"></div>
  <div class="tasks">Monitor Progress<br>Review Content<br>Track FEL<br>Assignments<br>Develop Budgets<br>Share with<br>Stakeholders</div>
  <svg width="443" height="246" viewBox="0 0 443 246" style="position:absolute;left:0;top:0">
    <defs><marker id="tip" markerWidth="6" markerHeight="6" refX="3" refY="3" orient="auto-start-reverse"><path d="M0,0 L6,3 L0,6 z" fill="var(--red)"/></marker></defs>
    <g stroke="var(--red)" stroke-width="3" fill="none">
      <line x1="124" y1="88" x2="140" y2="88" marker-start="url(#tip)" marker-end="url(#tip)"/>
      <line x1="316" y1="78" x2="238" y2="78" marker-end="url(#tip)"/>
      <line x1="188" y1="140" x2="188" y2="160" marker-end="url(#tip)"/>
      <line x1="246" y1="200" x2="282" y2="200" marker-end="url(#tip)"/>
      <line x1="395" y1="190" x2="395" y2="132" marker-end="url(#tip)"/>
      <line x1="30" y1="144" x2="30" y2="128" marker-end="url(#tip)"/>
    </g>
  </svg>
  <span class="brand" style="color:#e6f0f2">ZOL</span>
</section>

<section class="slide s-benefits">
  <h2>What are the benefits of having a “Remote Scheduler” within your organization?</h2>
  <ul class="benefits">
    <li>Reduced cost of operation and higher skilled scheduler…bigger bang for your buck!</li>
    <li>Only pay for the amount of work you need</li>
    <li>A lead or master scheduler available when you need them</li>
    <li>A well structured schedule following your company guidelines</li>
    <li>Consistency, your schedules will always be familiar and easy to understand</li>
  </ul>
  <div class="placeholder" role="img" aria-label="Silhouette of a person filled with horizontal blue and green bands"></div>
  <span class="brand" style="color:#e8efe6">ZOL</span>
</section>

</body>
</html>
```